Web-page design

We need a initial web design for our page kelbrook.com.au (which is not yet set up).
We provide consulting services for all kinds of problems in and between organisations.
Main focus is on conflict resolution but we also support companies on improving their operational performance.
We want to have the following page structure (and part of the project is to design the 8 pages):
- Home
- Services (we offer 3 main service areas - one per page)
- Case studies (one per page)
- Engaging us (our process)
- About Conflict & low performance
- Conflict resolution App
- About
- Contact (Email form)
- Our logo should be on each page.
The start page should include the following information:
- Twitter / Linkedin / facebook/ google + Links
- Telephone / Email or in general contact details
- News
- A quite prominent picture box with 3 alternating pics - each representing one of our service areas
- Link to our App
- Testimonials
It would be nice if the service pages would have an image header. Links to the information section (about conflict & low performance; and the app page) would be nice as well.
We like the following joomla designs: www.frandelthemes.com/itempreview/153
No need to copy it, it should just give you an idea.
We like the layout here with the picture and space for the case studies on the left. Somewhere beneath should be the 3 service areas with a picture each.
In terms of colors: our logo colours are Blue (RBG 8;44;80) and Orange (RGB 231;120;23). The orange could be used to emphasise certain things, however there should not be too much color.
Budget for images available, so please use placeholders or ask us for specific photos/images, if you need them for your design.
Updates
Hi, one more thing that we would like to have is the case studies not hidden behind a link "case studies" - we would like to have them individually linked prominent on the first page. There will be about 6-8 of them. Thats what we liked on the joomla template (the links left from the picture).
Hi, thanks very much for all the great proposals.
We are currently going through the selection process and will post our decision early next week.
Thanks again!
Wilma
Target Market(s)
- target customers are all different kinds of businesses and organisations (all industries, government, non-for-profit, ...) experiencing conflict and tension - be it with internal staff, amongst managers or board members, dysfunctional teams, between organizations or customers and organizations... examples could be bullying allegations, governmental negotiations with unions, disputes within organizations etc.
- also we will offer performance improvement services for organizations
- we will offer mediation, facilitation, negotiation, performance improvement services, conflict coaching, conflict management, change management services
- if comparable to anything - then to a law firm in terms of dealing with conflicts but its much less adversarial and much more about the people and their interests rather than about laws
- basically it's all kind of things you can do in order to solve disputes without involving lawyers and a court - so it's much cheaper and target is to find a solution all parties can live with rather than having a judge deciding about who wins and who looses
- performance management is more about analysing reasons for a lack of performance and setting up continous improvement systems, supporting change management, facilitating improvement workshops or strategic meetings, ...
Industry/Entity Type
Consulting
Look and feel

```html
<!DOCTYPE html>
<html lang="en">
<head>
<meta charset="utf-8">
<title>Harlow Brennan – Conflict Resolution &amp; Performance Consulting</title>
<link rel="stylesheet" href="https://fonts.googleapis.com/css2?family=Cabin:wght@400;500;600&family=Arimo:wght@400;700&display=swap">
<style>
:root{
  --navy:#082c50;
  --blue-heading:#1d3f63;
  --orange:#e77817;
  --text:#555;
  --text-soft:#666;
  --dark:#222;
  --panel:#f2f0f0;
  --panel-border:#dcdcdc;
  --hero-light:#f6f9fb;
  --hero-mid:#dfe9f1;
  --photo-tone:#c9d6e0;
}
*{box-sizing:border-box;margin:0;padding:0}
html,body{width:1029px;height:1200px;overflow:hidden;background:#fff}
body{font-family:"Arimo",Arial,sans-serif;color:var(--text)}
a{text-decoration:none;color:inherit}
.viewport{width:1029px;height:1200px;overflow:hidden;position:relative}
.page{width:1200px;height:1400px;position:absolute;left:0;top:0;transform:scale(.8575);transform-origin:0 0}
.abs{position:absolute}

.top-bar{left:100px;top:0;width:1000px;height:8px;background:var(--navy);border-radius:0 0 6px 6px}
.call{left:107px;top:53px;font-size:12px;color:#111}
.call span{font-style:italic;color:var(--orange);font-size:14px}
.util-nav{right:100px;top:58px;font-size:12px;color:#111}
.util-nav a{margin:0 6px}
.util-nav a:last-child{margin-right:0}

.brand{left:102px;top:112px;display:flex;align-items:center;gap:12px}
.brand-name{font-family:"Cabin",sans-serif;font-size:31px;color:var(--navy);letter-spacing:.5px}
.brand-mark{width:14px;height:14px;border-radius:50%;background:var(--navy)}
.brand-url{left:128px;top:162px;font-size:12px;letter-spacing:7.6px;color:var(--navy);font-weight:700}

.main-nav{right:103px;top:139px;display:flex;gap:24px;font-family:"Cabin",sans-serif;font-size:15px;color:#555;text-transform:uppercase}

.hero{left:0;top:190px;width:1200px;height:409px;
  background:repeating-linear-gradient(135deg,rgba(255,255,255,.25) 0 2px,transparent 2px 6px),
  linear-gradient(180deg,#fff 0%,var(--hero-light) 25%,var(--hero-mid) 100%)}
.hero-photo{left:150px;top:70px;width:560px;height:320px;border-radius:40px;
  background:radial-gradient(ellipse at 50% 50%,var(--photo-tone) 0%,rgba(220,230,238,.6) 55%,rgba(230,238,244,0) 75%)}
.hero-arrow{top:168px}
.hero-copy{left:812px;top:146px;font-family:"Cabin",sans-serif;font-size:25px;line-height:36px;color:#555}
.btn{left:811px;top:304px;width:150px;height:41px;background:var(--orange);color:#fff;font-family:"Cabin",sans-serif;font-size:18px;display:flex;align-items:center;justify-content:center;border-radius:2px}

.services{left:0;top:600px;width:1200px;height:318px;background:linear-gradient(180deg,#fff 60%,#efefef 100%)}
.dots{left:544px;top:614px;display:flex;gap:7px;z-index:5}
.dots i{width:14px;height:14px;border-radius:50%;border:1px solid #aaa;background:#fff}
.dots i.on{background:#555;border-color:#555}

.service{width:270px}
.service-icon{width:90px;height:86px;border-radius:6px}
.service h2{font-family:"Cabin",sans-serif;font-weight:400;font-size:17px;color:var(--blue-heading);margin-top:22px;text-transform:uppercase}
.service p{font-size:12px;line-height:20px;color:var(--text-soft);margin-top:10px;width:265px}
.read-more{display:inline-block;font-size:12px;color:var(--orange);text-decoration:underline;margin-top:17px}

.info-panel{left:128px;top:944px;width:942px;height:206px;background:var(--panel);border:1px solid var(--panel-border);box-shadow:0 3px 0 #d5d5d5}
.info-col{top:16px;width:264px}
.info-col h3{font-family:"Cabin",sans-serif;font-weight:400;font-size:17px;color:#444;height:30px}
.info-col .rule{height:6px;background:var(--orange)}
.info-col p{font-size:12px;line-height:20px;color:var(--text-soft);margin-top:19px}
.info-col .read-more{color:#888;margin-top:7px}
.app-visual{margin-top:14px;width:262px;height:122px;background:linear-gradient(120deg,#8d9297 0%,#c4c9cd 55%,#a9b6c2 100%)}

.case-panel{left:128px;top:1175px;width:943px;height:208px;border:1px solid var(--orange);border-radius:3px;background:#fff}
.case-panel h3{position:absolute;left:19px;top:13px;font-family:"Cabin",sans-serif;font-weight:400;font-size:17px;color:var(--blue-heading)}
.case-rule{left:19px;top:45px;width:908px;height:1px;background:#aaa}
.case{top:62px;width:160px}
.case h4{font-family:"Cabin",sans-serif;font-weight:600;font-size:13.5px;color:var(--dark)}
.case p{font-size:12px;line-height:20px;color:#555;margin-top:2px}
.case .read-more{margin-top:12px;margin-left:-2px}
.case-arrow{top:1264px;z-index:5}
</style>
</head>
<body>
<div class="viewport">
<div class="page">

  <div class="abs top-bar"></div>
  <div class="abs call">Call us at: <span>0987 654 321</span></div>
  <nav class="abs util-nav"><a href="#">Home</a> | <a href="#">About Us</a> | <a href="#">Contact Us</a></nav>

  <a class="abs brand" href="#"><span class="brand-mark"></span><span class="brand-name">HARLOW BRENNAN</span></a>
  <div class="abs brand-url">www.kelbrook.com.au</div>

  <nav class="abs main-nav">
    <a href="#">Services</a><a href="#">Case Studies</a><a href="#">Engaging Us</a><a href="#">About Conflict</a><a href="#">Resolution App</a>
  </nav>

  <section class="abs hero">
    <div class="abs hero-photo" role="img" aria-label="Photo of two consultants reviewing documents at a laptop"></div>
    <svg class="abs hero-arrow" style="left:104px" width="22" height="56" viewBox="0 0 22 56"><path d="M20 2 L6 28 L20 54 L14 54 L2 28 L14 2Z" fill="#c3ccd4"/></svg>
    <svg class="abs hero-arrow" style="left:1080px" width="22" height="56" viewBox="0 0 22 56"><path d="M2 2 L16 28 L2 54 L8 54 L20 28 L8 2Z" fill="#c3ccd4"/></svg>
    <p class="abs hero-copy">See how we provide<br>innovative services to<br>your business with<br>economical price</p>
    <a class="abs btn" href="#">Contact Us Now</a>
  </section>

  <section class="abs services">
    <article class="abs service" style="left:134px;top:40px">
      <div class="service-icon" role="img" aria-label="Icon of a magnifying glass over a bar chart" style="background:radial-gradient(circle at 40% 40%,#d8eef5 0 30%,#e9eef1 60%,#fff 100%)"></div>
      <h2>Market Research Services</h2>
      <p>some lorem ipsum text will be here some lorem ipsum text will be here some lorem ipsum text will be here some lorem ipsum text will be here some lorem ipsum text will be here</p>
      <a class="read-more" href="#">read more</a>
    </article>
    <article class="abs service" style="left:475px;top:40px">
      <div class="service-icon" role="img" aria-label="Illustration of a head silhouette filled with marketing words" style="width:70px;background:linear-gradient(180deg,#3a3f3a,#111)"></div>
      <h2>Marketing Plans Services</h2>
      <p>some lorem ipsum text will be here some lorem ipsum text will be here some lorem ipsum text will be here some lorem ipsum text will be here some lorem ipsum text will be here</p>
      <a class="read-more" href="#">read more</a>
    </article>
    <article class="abs service" style="left:806px;top:40px">
      <div class="service-icon" role="img" aria-label="Icon of an orange folder with reports" style="background:linear-gradient(160deg,#f2c25b,#d98d14)"></div>
      <h2>Marketing Project Services</h2>
      <p>some lorem ipsum text will be here some lorem ipsum text will be here some lorem ipsum text will be here some lorem ipsum text will be here some lorem ipsum text will be here</p>
      <a class="read-more" href="#">read more</a>
    </article>
  </section>

  <div class="abs dots" aria-label="Slide selector"><i class="on"></i><i></i><i></i><i></i></div>

  <section class="abs info-panel">
    <div class="abs info-col" style="left:21px">
      <h3>News and update</h3><div class="rule"></div>
      <p>some lorem ipsum text will be here some lorem ipsum text will be here some lorem ipsum text will be here some lorem ipsum text will be here some lorem ipsum text will be here lorem ipsum text will be here lorem ipsum text will be here</p>
      <a class="read-more" href="#">read more</a>
    </div>
    <div class="abs info-col" style="left:332px">
      <h3>Testimonials</h3><div class="rule"></div>
      <p>some lorem ipsum text will be here some lorem ipsum text will be here some lorem ipsum text will be here some lorem ipsum text will be here some lorem ipsum text will be here lorem ipsum text will be here lorem ipsum text will be here</p>
      <a class="read-more" href="#">read more</a>
    </div>
    <div class="abs info-col" style="left:643px">
      <h3>Conflict Resolution App</h3><div class="rule"></div>
      <div class="app-visual" role="img" aria-label="Photo of a businessman touching a screen with strategy diagrams"></div>
    </div>
  </section>

  <section class="abs case-panel">
    <h3>Case Studies</h3>
    <div class="abs case-rule"></div>
    <article class="abs case" style="left:27px"><h4>Case study Heading</h4><p>lorem ipsum text will be here lorem ipsum text will be here lorem ipsum text will be here lorem ipsum text will be here</p><a class="read-more" href="#">read more..</a></article>
    <article class="abs case" style="left:208px"><h4>Case study Heading</h4><p>lorem ipsum text will be here lorem ipsum text will be here lorem ipsum text will be here lorem ipsum text will be here</p><a class="read-more" href="#">read more..</a></article>
    <article class="abs case" style="left:388px"><h4>Case study Heading</h4><p>lorem ipsum text will be here lorem ipsum text will be here lorem ipsum text will be here lorem ipsum text will be here</p><a class="read-more" href="#">read more..</a></article>
    <article class="abs case" style="left:573px"><h4>Case study Heading</h4><p>lorem ipsum text will be here lorem ipsum text will be here lorem ipsum text will be here lorem ipsum text will be here</p><a class="read-more" href="#">read more..</a></article>
    <article class="abs case" style="left:758px"><h4>Case study Heading</h4><p>lorem ipsum text will be here lorem ipsum text will be here lorem ipsum text will be here lorem ipsum text will be here</p><a class="read-more" href="#">read more..</a></article>
  </section>

  <svg class="abs case-arrow" style="left:127px" width="11" height="44" viewBox="0 0 11 44" aria-label="Previous case studies"><path d="M0 0 L11 22 L0 44Z" fill="#082c50"/></svg>
  <svg class="abs case-arrow" style="left:1067px" width="11" height="44" viewBox="0 0 11 44" aria-label="Next case studies"><path d="M11 0 L0 22 L11 44Z" fill="#082c50"/></svg>

</div>
</div>
</body>
</html>
```